Improve the existing label for Brenovitralica company.

The BVT company is launching a new product and needs the label for the product to be re-designed. Candidates should maintain the actual texts, and see if they can improve on the LumaVetra Logo and the Biodegradable logo.
For the LumaVetra Logo please use a diamond (any diamont will suffice)
The label should maintain the blue on white aspect and can use blue gradients.(monochromatic).
the white part of the label and the bottle will be transparent, and the liquid inside the bottle is blue.

The product is a monitor/tv/cell/tablet screen cleaner.
The label size is (7 cm in heigh)t and (3,8 cm in lenght).

The actual label is attached.

Thanks in advance for your designs.

```html
<!DOCTYPE html>
<html lang="pt">
<head>
<meta charset="utf-8">
<title>LumaVetra – Linha Celeste</title>
<link rel="stylesheet" href="https://fonts.googleapis.com/css2?family=Abril+Fatface&family=Archivo+Black&family=Fredoka:wght@500&display=swap">
<style>
  :root {
    --brand-blue: #1574bb;
    --paper: #ffffff;
  }
  html, body {
    margin: 0;
    padding: 0;
    width: 1200px;
    height: 2208px;
    overflow: hidden;
    background: var(--paper);
  }
  .label {
    position: relative;
    width: 1200px;
    height: 2208px;
    background: var(--paper);
    color: var(--brand-blue);
  }
  .label__frame-outer {
    position: absolute;
    inset: 8px;
    border: 11px solid var(--brand-blue);
  }
  .label__frame-inner {
    position: absolute;
    inset: 30px;
    border: 4px solid var(--brand-blue);
  }
  .brand-name {
    position: absolute;
    left: 0;
    top: 190px;
    width: 1200px;
    height: 180px;
  }
  .brand-name text {
    font-family: "Abril Fatface", serif;
    font-size: 170px;
    fill: var(--brand-blue);
  }
  .product-line {
    position: absolute;
    left: 0;
    top: 515px;
    width: 100%;
    text-align: center;
    font-family: "Fredoka", sans-serif;
    font-weight: 500;
    font-size: 76px;
    line-height: 1;
  }
  .eco-badge {
    position: absolute;
    left: 310px;
    top: 770px;
    width: 580px;
    height: 580px;
  }
  .uses {
    position: absolute;
    left: 0;
    top: 1486px;
    width: 100%;
    margin: 0;
    text-align: center;
    font-family: "Archivo Black", sans-serif;
    font-size: 68px;
    line-height: 88px;
    letter-spacing: -3px;
  }
  .volume {
    position: absolute;
    left: 0;
    top: 2052px;
    width: 100%;
    text-align: center;
    font-family: "Archivo Black", sans-serif;
    font-size: 40px;
    line-height: 1;
    letter-spacing: -1px;
  }
</style>
</head>
<body>
  <main class="label">
    <div class="label__frame-outer"></div>
    <div class="label__frame-inner"></div>

    <svg class="brand-name" viewBox="0 0 1200 180" aria-label="LumaVetra">
      <text x="600" y="150" text-anchor="middle" textLength="1010" lengthAdjust="spacingAndGlyphs">LumaVetra</text>
    </svg>

    <div class="product-line">Linha Celeste</div>

    <svg class="eco-badge" viewBox="0 0 580 580" role="img" aria-label="Selo biodegradável">
      <circle cx="290" cy="290" r="280" fill="none" stroke="var(--brand-blue)" stroke-width="7"/>
      <circle cx="290" cy="290" r="146" fill="none" stroke="var(--brand-blue)" stroke-width="72"/>
    </svg>

    <p class="uses">
      PARA LIMPEZA DE<br>
      MONITORES - TV - LCD<br>
      LED - PLASMA - OCULOS<br>
      CAMERAS - TABLETS<br>
      CELULARES
    </p>

    <div class="volume">CONTEM 60 ml</div>
  </main>
</body>
</html>
```